Luftpolster-Versandtaschen  designen
Luftpolster-Versandtaschen designen
Zielgruppe
Es ist eine natürliche Schmerzsalbe entwickelt und hergestellt in Deutschland.
Die PELOR Salbe gibt ein zuverlässige Gefühl, durch ein innovatives Naturprodukt erstaunlich schnelle, wirkungsvolle Hilfe bei Schmerzen des Bewegungsapparates und bei Hautschäden zu erhalten und dabei gleichzeitig die Haut zu pflegen.
Aufgabenstellung
Wir möchten unsere Luftpolster-Versandtaschen gestalten lassen und das Corporate Design dort platzieren.
Ziel soll sein, das der Kunde eine hohe Aufmerksamkeit schon, vor dem Öffnen und das Vertrauen erhöht, schnelle Wiedererkennung der Marke Pelor Naturbalsam.
Die Druckdateien benötigen wir als pdf oder jedwede andere Datei mit einer Mindestauflösung von 300 dpi. Die Farbdarstellung erfolgt in CMYK. Alle Grafiken werden mittig platziert und proportional angepasst. Die genauen Maße der Versandtaschen bitte den Dokument vorlage_packbag entnehmen.
Farben / Texte / Bilder können von den Dokument (neue_webseite_alle_seiten_uebersicht) verwendet werden.
Bitte die Datei (vorlage_packbag_14d.pdf) von der Druckerei beachten.

```html
<!DOCTYPE html>
<html lang="de">
<head>
<meta charset="utf-8">
<title>Pelor Naturbalsam – Versandtasche</title>
<link href="https://fonts.googleapis.com/css2?family=Open+Sans:ital,wght@0,400;0,600;0,700;0,800;1,400;1,600;1,700&family=Arimo:wght@700&display=swap" rel="stylesheet">
<style>
  :root {
    --page: #ffffff;
    --bleed: #d9d9d9;
    --trim: #2e3381;
    --orange-deep: #ec6e1a;
    --orange-mid: #f7b446;
    --orange-edge: #f4a457;
    --icon: #f0b560;
    --ink: #111111;
    --grey-text: #8d8d8d;
    --white: #ffffff;
  }
  * { margin: 0; padding: 0; box-sizing: border-box; }
  html, body { width: 1200px; height: 1200px; overflow: hidden; background: var(--page); }
  body { position: relative; font-family: "Open Sans", Arial, sans-serif; }

  .bag-template {
    position: absolute; left: 361px; top: 264px; width: 485px; height: 678px;
    background: var(--bleed);
  }
  .side-label {
    position: absolute; left: 361px; top: 281px; width: 548px;
    text-align: center; font-family: "Arimo", Arial, sans-serif;
    font-weight: 700; font-size: 13px; color: var(--ink); letter-spacing: 0.2px;
  }
  .print-area {
    position: absolute; left: 382px; top: 329px; width: 444px; height: 591px;
    background: var(--white); border: 2px solid var(--trim);
  }

  .brand {
    position: absolute; left: 535px; top: 420px;
    display: flex; align-items: center; gap: 8px;
  }
  .brand-dot { width: 24px; height: 24px; border-radius: 50%; background: var(--orange-mid); }
  .brand-name {
    font-weight: 800; font-size: 17px; color: var(--ink); letter-spacing: 0.3px; line-height: 1;
  }

  .hero {
    position: absolute; left: 484px; top: 537px; width: 238px; height: 231px;
    background: linear-gradient(90deg, var(--orange-edge) 0%, var(--orange-mid) 22%, var(--orange-mid) 78%, var(--orange-edge) 100%);
  }
  .hero-title {
    position: absolute; left: 35px; top: 66px;
    font-weight: 800; font-size: 35px; line-height: 29px; color: var(--orange-deep);
  }
  .hero-title span { display: block; }
  .hero-title .line-1 { letter-spacing: 2.5px; }
  .hero-title .line-2 { letter-spacing: 9px; }
  .hero-claim {
    position: absolute; left: 35px; top: 130px;
    font-weight: 800; font-size: 19.5px; line-height: 21px; color: var(--white); letter-spacing: 0.4px;
  }

  .promise {
    position: absolute; left: 485px; top: 781px;
    font-style: italic; font-weight: 600; font-size: 12.5px; line-height: 16.5px;
    color: var(--grey-text); letter-spacing: 1.4px;
  }

  .benefits { position: absolute; left: 444px; top: 823px; width: 360px; height: 26px; }
  .benefit { position: absolute; top: 0; display: flex; align-items: center; gap: 3px; }
  .benefit svg { width: 26px; height: 26px; display: block; }
  .benefit-label {
    font-style: italic; font-weight: 700; font-size: 5.2px; color: var(--grey-text); letter-spacing: 0.3px;
    white-space: nowrap;
  }
  .benefit.relax { left: 0; }
  .benefit.natural { left: 119px; }
  .benefit.care { left: 237px; }
</style>
</head>
<body>
  <div class="bag-template"></div>
  <div class="side-label">OBEN</div>
  <div class="print-area"></div>

  <div class="brand">
    <div class="brand-dot"></div>
    <div class="brand-name">PELOR Naturbalsam</div>
  </div>

  <div class="hero">
    <h1 class="hero-title"><span class="line-1">ALWAYS</span><span class="line-2">PELOR!</span></h1>
    <p class="hero-claim">MIT DER KRAFT<br>AUS DER NATUR</p>
  </div>

  <p class="promise">Hält jung, macht beweglich<br>Mit der 10-Kräuter-Aktivformel</p>

  <div class="benefits">
    <div class="benefit relax">
      <svg viewBox="0 0 26 26" aria-hidden="true">
        <circle cx="13" cy="13" r="12.5" fill="var(--icon)"/>
        <path d="M13 6 C11.5 8.5 11 9.5 11 10.5 a2 2 0 0 0 4 0 C15 9.5 14.5 8.5 13 6Z" fill="none" stroke="#fff" stroke-width="0.9"/>
        <path d="M6 17 Q9 14 12 16 L16 16 Q17 17 16 18 L12 18 M16 17.5 L19.5 15.5 Q21 15.5 20 17 L15 20 L8 20" fill="none" stroke="#fff" stroke-width="0.9" stroke-linecap="round"/>
      </svg>
      <span class="benefit-label">ENTSPANNT UND REGENERIERT</span>
    </div>
    <div class="benefit natural">
      <svg viewBox="0 0 26 26" aria-hidden="true">
        <circle cx="13" cy="13" r="12.5" fill="var(--icon)"/>
        <path d="M13 20 L13 12" stroke="#fff" stroke-width="0.9" fill="none"/>
        <path d="M13 13 Q7 14 6.5 9 Q11.5 8.5 13 13Z" fill="none" stroke="#fff" stroke-width="0.9"/>
        <path d="M13 12 Q14 7 19.5 7 Q19 12 13 12Z" fill="none" stroke="#fff" stroke-width="0.9"/>
      </svg>
      <span class="benefit-label">100% NATUR</span>
    </div>
    <div class="benefit care">
      <svg viewBox="0 0 26 26" aria-hidden="true">
        <circle cx="13" cy="13" r="12.5" fill="var(--icon)"/>
        <path d="M6 12.5 L20 12.5 Q19.5 18 15 18.5 L11 18.5 Q6.5 18 6 12.5Z" fill="none" stroke="#fff" stroke-width="0.9"/>
        <path d="M10 20 L16 20" stroke="#fff" stroke-width="0.9"/>
        <path d="M14 12 L16.5 6.5" stroke="#fff" stroke-width="1.1" stroke-linecap="round"/>
      </svg>
      <span class="benefit-label">STÄRKT, PFLEGT, SCHÜTZT</span>
    </div>
  </div>
</body>
</html>
```